Selka Marven Photography Business Card

I need a new business card/ possibly design to use for other marking materials ... I have included my logo below in a few different colors, but can also provide the logo in additional colors and sizes. I would love a card the expresses clean, simple and classy.

Target Market(s)

Portrait photography clients, child photography clients

Industry/Entity Type

Photographer

Contact Information for Business Card

Selka Marven Photography, Halvern MA, www.selkamarvenphotography-demo.com
T. 555-203-1946 E. selkamarvenphoto@mailbox-demo.com

Colors
33b8a4
eea4c8
5c5c5c

Requirements
Must have
• I would like to include my logo on card.
Nice to have
• I also like the color brown as well as the choices below. I would like a simple, elegant card, something classy.

```html
<!DOCTYPE html>
<html lang="en">
<head>
<meta charset="utf-8">
<title>Selka Marven Photography – Business Card</title>
<link rel="stylesheet" href="https://fonts.googleapis.com/css2?family=Roboto+Condensed:wght@400&family=Montserrat:wght@400&family=Sacramento&display=swap">
<style>
  :root {
    --backdrop: #d9d9d9;
    --card: #ffffff;
    --teal: #4fb5a8;
    --ink: #5c5c5c;
    --muted: #7a7a7a;
    --portrait-dark: #3a2f2e;
    --portrait-skin: #e6b9a3;
    --portrait-hair: #9a7550;
  }
  html, body {
    margin: 0;
    padding: 0;
    overflow: hidden;
  }
  body {
    width: 1200px;
    height: 900px;
    background: var(--backdrop);
    position: relative;
  }
  .card {
    position: absolute;
    top: 166px;
    width: 325px;
    height: 568px;
    background: var(--card);
    box-shadow: 0 2px 6px rgba(0,0,0,0.25);
  }
  .card--front { left: 265px; }
  .card--back { left: 610px; }

  .front-name {
    position: absolute;
    top: 28px;
    left: 0;
    width: 100%;
    text-align: center;
    font-family: "Sacramento", cursive;
    font-size: 50px;
    line-height: 1;
    color: var(--teal);
    letter-spacing: 3px;
  }
  .front-title {
    position: absolute;
    top: 77px;
    left: 0;
    width: 100%;
    text-align: center;
    font-family: "Montserrat", sans-serif;
    font-size: 16px;
    letter-spacing: 1.8px;
    color: var(--ink);
  }
  .brand-mark {
    position: absolute;
    top: 422px;
    right: 31px;
    width: 220px;
    text-align: center;
    font-family: "Roboto Condensed", sans-serif;
    font-weight: 400;
    color: var(--teal);
    line-height: 1.2;
  }
  .brand-mark__name {
    display: block;
    font-size: 20px;
  }
  .brand-mark__trade {
    display: block;
    font-size: 10px;
    letter-spacing: 2.4px;
  }
  .contact {
    position: absolute;
    top: 476px;
    right: 31px;
    text-align: right;
    font-family: "Roboto Condensed", sans-serif;
    font-size: 14.5px;
    line-height: 18.5px;
    letter-spacing: 0.6px;
    color: var(--muted);
  }
  .contact p { margin: 0; }
  .contact__sep { padding: 0 5px; }

  .portrait {
    position: absolute;
    top: 20px;
    left: 19px;
    width: 286px;
    height: 528px;
    background:
      radial-gradient(ellipse 60% 45% at 45% 55%, var(--portrait-skin) 0%, rgba(230,185,163,0.6) 55%, rgba(230,185,163,0) 80%),
      linear-gradient(180deg, var(--portrait-hair) 0%, var(--portrait-dark) 22%, #6e5550 60%, #c9a596 100%);
  }
</style>
</head>
<body>
  <section class="card card--front" aria-label="Business card front">
    <div class="front-name">selka marven</div>
    <div class="front-title">PHOTOGRAPER</div>

    <div class="brand-mark">
      <span class="brand-mark__name">Selka Marven</span>
      <span class="brand-mark__trade">PHOTOGRAPHY</span>
    </div>

    <div class="contact">
      <p>555-203-1946<span class="contact__sep">|</span>Halvern MA</p>
      <p>selkamarvenphoto@mailbox-demo.com</p>
      <p>www.selkamarvenphotography-demo.com</p>
    </div>
  </section>

  <section class="card card--back" aria-label="Business card back">
    <div class="portrait" role="img" aria-label="Portrait photograph of the photographer in a sequined top and headband against a dark backdrop"></div>
  </section>
</body>
</html>
```